Our architectural studio needs a new business card

We need a business card design for our studio based in Waterloo in Belgium. We are active in architecture, design and installation.
Our works are contemporary and minimalist. our clients are refined and cultured.
Our business card must be minimalist and refined.

Project Deadline Extended
Reason: Some designers have accepted my invitation but they don't have all replied. I want to give them a chance to make one proposal. Paul

Target Market(s)

architecture

Industry/Entity Type

Business

Contact Information for Business Card

studio: paul dornevaux studio
paul dornevaux, architecte
M. +32 471 586 927
F. +322 619 4850
www.pauldornevaux-example.com
paul@pauldornevaux-example.com
14 rue des Marronniers
1420 Waterloo
Belgium

Font styles to use
Sans Serif

Requirements
Must have
• simple, minimalist, clear, elegant and chic! Black and white
Nice to have
• embossed logo, other format like a square for example
Should not have
• color, fantasy, curves, ...

```html
<!DOCTYPE html>
<html lang="fr">
<head>
<meta charset="utf-8">
<title>Paul Dornevaux Studio — Business Card</title>
<link rel="stylesheet" href="https://fonts.googleapis.com/css2?family=Exo+2:wght@700&family=Jost:wght@400;500&family=Arimo:wght@400&display=swap">
<style>
  :root {
    --bg: #3b3b3b;
    --card-dark: #262626;
    --panel-light: #a4a4a4;
    --panel-mid: #8c8c8c;
    --mark: #5d5759;
    --name: #8e8e8e;
    --contact: #a8a8a8;
  }
  * { box-sizing: border-box; margin: 0; padding: 0; }
  html, body { width: 1200px; height: 1000px; overflow: hidden; }
  body { background: var(--bg); position: relative; font-family: "Arimo", Arial, sans-serif; }

  .card { position: absolute; background: var(--card-dark); box-shadow: 0 18px 40px rgba(0,0,0,.45); }

  /* Front (vertical) */
  .card-front { left: 70px; top: 150px; width: 400px; height: 700px; }
  .card-front .panel {
    position: absolute; left: 14px; top: 0; width: 362px; height: 100%;
    background: linear-gradient(180deg, var(--panel-light), var(--panel-mid));
  }
  .front-mark {
    position: absolute; left: 150px; top: 250px;
    display: flex; align-items: center; gap: 18px;
    transform: rotate(90deg); transform-origin: left top;
    left: 255px;
  }
  .mark-square { width: 22px; height: 22px; background: var(--mark); flex: none; }
  .studio-name {
    font-family: "Jost", sans-serif; font-weight: 500; color: var(--mark);
    letter-spacing: 2px; text-transform: uppercase; white-space: nowrap; font-size: 15px;
  }

  /* Back (horizontal) */
  .card-back { left: 510px; top: 310px; width: 640px; height: 370px; }
  .card-back .panel {
    position: absolute; left: 14px; top: 14px; width: 240px; height: 342px;
    background: linear-gradient(180deg, var(--panel-light), var(--panel-mid));
  }
  .back-mark { position: absolute; left: 16px; top: 150px; display: flex; align-items: center; gap: 10px; }
  .back-mark .studio-name { font-size: 12px; letter-spacing: 1.5px; }
  .back-mark .mark-square { width: 16px; height: 16px; }

  .identity { position: absolute; left: 292px; top: 46px; }
  .person-name {
    font-family: "Exo 2", sans-serif; font-weight: 700; color: var(--name);
    font-size: 42px; line-height: 1; letter-spacing: .5px;
  }
  .person-role {
    font-family: "Exo 2", sans-serif; font-weight: 700; color: var(--name);
    font-size: 21px; margin-top: 2px;
  }

  .contact { position: absolute; left: 262px; top: 250px; list-style: none; }
  .contact li { display: flex; align-items: center; gap: 14px; color: var(--contact); font-size: 16px; line-height: 22px; }
  .contact svg { width: 14px; height: 14px; fill: var(--contact); flex: none; }
</style>
</head>
<body>
  <section class="card card-front" aria-label="Card front">
    <div class="panel">
      <div class="front-mark">
        <span class="mark-square"></span>
        <span class="studio-name">paul dornevaux studio</span>
      </div>
    </div>
  </section>

  <section class="card card-back" aria-label="Card back">
    <div class="panel">
      <div class="back-mark">
        <span class="mark-square"></span>
        <span class="studio-name">paul dornevaux studio</span>
      </div>
    </div>

    <div class="identity">
      <h1 class="person-name">paul dornevaux</h1>
      <p class="person-role">architecte</p>
    </div>

    <ul class="contact">
      <li>
        <svg viewBox="0 0 24 24" aria-hidden="true"><path d="M6.6 10.8a15 15 0 0 0 6.6 6.6l2.2-2.2c.3-.3.7-.4 1-.2 1.1.4 2.3.6 3.6.6.6 0 1 .4 1 1V20c0 .6-.4 1-1 1A17 17 0 0 1 3 4c0-.6.4-1 1-1h3.5c.6 0 1 .4 1 1 0 1.3.2 2.5.6 3.6.1.3 0 .7-.2 1z"/></svg>
        <span>+32 471 586 927 &nbsp;| +322 619 4850</span>
      </li>
      <li>
        <svg viewBox="0 0 24 24" aria-hidden="true"><path d="M2 5h20v14H2zm2 2v.4l8 5 8-5V7zm0 2.8V17h16V9.8l-8 5z"/></svg>
        <span>info@pauldornevaux-example.com</span>
      </li>
      <li>
        <svg viewBox="0 0 24 24" aria-hidden="true"><path d="M12 2a7 7 0 0 0-7 7c0 5 7 13 7 13s7-8 7-13a7 7 0 0 0-7-7zm0 9.5A2.5 2.5 0 1 1 12 6.5a2.5 2.5 0 0 1 0 5z"/></svg>
        <span>14 rue des Marronniers Waterloo 1420</span>
      </li>
      <li>
        <svg viewBox="0 0 24 24" aria-hidden="true"><path d="M12 2a10 10 0 1 0 0 20 10 10 0 0 0 0-20zm0 2a8 8 0 0 1 0 16 8 8 0 0 1 0-16zM4 12h16v1.5H4zM11.2 4h1.6v16h-1.6z"/></svg>
        <span>www.pauldornevaux-example.com</span>
      </li>
    </ul>
  </section>
</body>
</html>
```